Designer my sauce product Label

Hi there, I looking for someone to design my BBQ sauce bottle, I need it to be eye catching, creative and new modern. I have a standard 150ml bottle. The suace is called velquino sauce. I would like my logo to be on the bottle but not to large, I have also added examples of other designs that I like, My label has to be current with the market at the moment. Bottle attached

Target Market(s)

My target market is the early 20's to eary 30's, people that liek to eat and try new things

Industry/Entity Type

Fast Food Restaurant

Requirements
Must have
• Must have colour and be creative
Nice to have
• It would be nice to see some little images
Should not have
• N/A

```html
<!DOCTYPE html>
<html lang="en">
<head>
<meta charset="UTF-8">
<title>Velquino BBQ Sauce Label</title>
<link rel="stylesheet" href="https://fonts.googleapis.com/css2?family=Alfa+Slab+One&family=Oswald:wght@500&display=swap">
<style>
  :root {
    --backdrop: #ecebea;
    --label-cream: #efe1c3;
    --label-edge: #4a1d18;
    --label-deep: #2c0f0d;
    --ink: #2b1b17;
    --sauce-red: #c3302a;
    --tool-shade: rgba(43, 27, 23, 0.16);
  }
  * { margin: 0; padding: 0; box-sizing: border-box; }
  html, body {
    width: 1200px;
    height: 2212px;
    overflow: hidden;
    background: var(--backdrop);
  }
  .artboard {
    position: relative;
    width: 1200px;
    height: 2212px;
  }

  /* Neck label */
  .neck-label {
    position: absolute;
    left: 330px;
    top: 130px;
    width: 540px;
    height: 300px;
    border-radius: 28px;
    background: radial-gradient(ellipse at 50% 50%, var(--label-cream) 0%, #e2cda4 60%, var(--label-edge) 100%);
    overflow: hidden;
  }
  .neck-label .tools-art {
    position: absolute;
    left: 170px;
    top: 30px;
    width: 200px;
    height: 110px;
    border-radius: 50%;
    background: radial-gradient(ellipse, var(--tool-shade), transparent 70%);
  }
  .neck-label .neck-name {
    position: absolute;
    left: 0;
    right: 0;
    top: 140px;
    text-align: center;
    font-family: "Alfa Slab One", serif;
    font-size: 64px;
    letter-spacing: 2px;
    color: var(--ink);
  }

  /* Main label */
  .main-label {
    position: absolute;
    left: 100px;
    top: 560px;
    width: 1000px;
    height: 1480px;
    border-radius: 24px;
    background: radial-gradient(ellipse 60% 55% at 50% 42%, var(--label-cream) 0%, #e6d2ab 45%, #8a4a35 80%, var(--label-deep) 100%);
    overflow: hidden;
  }
  .brand-mark {
    position: absolute;
    left: 0;
    right: 0;
    top: 120px;
    display: flex;
    justify-content: center;
    align-items: center;
    gap: 18px;
  }
  .brand-mark .dot {
    width: 56px;
    height: 56px;
    border-radius: 50%;
    background: var(--ink);
  }
  .brand-mark .brand-name {
    font-family: "Alfa Slab One", serif;
    font-size: 40px;
    color: var(--ink);
  }
  .tools-art {
    position: absolute;
    left: 130px;
    top: 300px;
    width: 740px;
    height: 700px;
    border-radius: 50%;
    background: radial-gradient(ellipse, var(--tool-shade), transparent 70%);
  }
  .product-name,
  .product-type,
  .product-kind {
    position: absolute;
    left: 0;
    right: 0;
    text-align: center;
    font-family: "Alfa Slab One", serif;
  }
  .product-name {
    top: 410px;
    font-size: 130px;
    letter-spacing: 4px;
    color: var(--ink);
  }
  .product-type {
    top: 560px;
    font-size: 180px;
    letter-spacing: 6px;
    color: var(--sauce-red);
  }
  .product-kind {
    top: 780px;
    font-size: 92px;
    letter-spacing: 22px;
    color: var(--ink);
  }
  .claim,
  .net-weight {
    position: absolute;
    left: 0;
    right: 0;
    text-align: center;
    font-family: "Oswald", sans-serif;
    font-weight: 500;
    color: var(--ink);
    letter-spacing: 3px;
  }
  .claim { top: 1010px; font-size: 34px; }
  .net-weight { top: 1060px; font-size: 34px; }
</style>
</head>
<body>
  <div class="artboard">
    <div class="neck-label">
      <div class="tools-art" role="img" aria-label="Small crossed grill spatula and fork illustration"></div>
      <div class="neck-name">VELQUINO</div>
    </div>

    <div class="main-label">
      <div class="brand-mark">
        <span class="dot"></span>
        <span class="brand-name">Velquino</span>
      </div>
      <div class="tools-art" role="img" aria-label="Crossed grill spatula and fork illustration"></div>
      <div class="product-name">VELQUINO</div>
      <div class="product-type">BBQ</div>
      <div class="product-kind">SAUCE</div>
      <div class="claim">ALL NATURAL</div>
      <div class="net-weight">NET WT 16.5 OZ (467 G)</div>
    </div>
  </div>
</body>
</html>
```